Business Card Design Project

Hi
I'm currently getting a logo designed which will go on the front. It is designed for s
Fitness instructor/ personal training business.
On the back I would like written:
Boxing for Fitness
Aqua Fitness Professional
PersonalisedTraining 1/1 or Small Group outdoor training
Fun and unique workouts
Weight loss/ Strength training

Also I need on there my details
minaharper27@quillbox.net
0427 395 108
FB Mina Motion

Reason: I would like to extend the deadline to give extra days after I have confirmed the logo in two days

Target Market(s)

Mostly women aged between 20-50

Industry/Entity Type

Training

Font styles to use
Sans Serif

Requirements
Must have
• My logo ( I have attached my favourite logo options )
My details

```html
<!DOCTYPE html>
<html lang="en">
<head>
<meta charset="utf-8">
<title>Mina Motion — Business Card</title>
<link rel="stylesheet" href="https://fonts.googleapis.com/css2?family=Mulish:wght@400;600;700&display=swap">
<style>
  :root {
    --bg: #ecebe8;
    --card: #ffffff;
    --pink: #d77dbd;
    --pink-deep: #c4469f;
    --brand-pink: #e2559e;
    --mark-pink: #ef8fbf;
    --blue: #1f4f9a;
    --ink: #2a2a3a;
  }
  * { box-sizing: border-box; margin: 0; padding: 0; }
  html, body {
    width: 1200px; height: 738px; overflow: hidden;
    background: var(--bg);
    font-family: "Mulish", Arial, sans-serif;
    color: var(--ink);
  }
  .canvas { position: relative; width: 1200px; height: 738px; }
  .card {
    position: absolute; top: 214px;
    width: 540px; height: 310px;
    background: var(--card);
    overflow: hidden;
    box-shadow: 0 6px 18px rgba(0,0,0,.16);
  }
  .card--front { left: 40px; }
  .card--back { left: 620px; }
  .card__shapes { position: absolute; inset: 0; }

  .brand {
    position: absolute; left: 120px; top: 78px;
    display: flex; align-items: center; gap: 18px;
  }
  .brand__dot {
    width: 92px; height: 92px; border-radius: 50%;
    background: var(--mark-pink);
  }
  .brand__name {
    font-weight: 700; font-size: 40px; color: var(--brand-pink);
    letter-spacing: .5px;
  }

  .contact { position: absolute; font-size: 17px; line-height: 1.3; color: var(--ink); }
  .card--front .contact { left: 22px; bottom: 16px; }
  .card--back .contact { right: 20px; bottom: 16px; text-align: right; }

  .services {
    position: absolute; left: 30px; top: 64px;
    list-style: none; font-size: 15px; line-height: 1.75;
  }
  .services li { display: flex; align-items: center; gap: 10px; }
  .services li::before {
    content: ""; width: 9px; height: 9px; border-radius: 50%;
    background: var(--brand-pink); flex: none;
  }
</style>
</head>
<body>
<main class="canvas">

  <section class="card card--front" aria-label="Card front">
    <svg class="card__shapes" viewBox="0 0 540 310" aria-hidden="true">
      <line x1="0" y1="12" x2="540" y2="12" stroke="var(--blue)" stroke-width="3"/>
      <line x1="0" y1="20" x2="540" y2="20" stroke="var(--blue)" stroke-width="2"/>
      <path d="M0,205 Q260,275 540,140 L540,310 L0,310 Z" fill="var(--pink)"/>
      <path d="M0,205 Q260,275 540,140" fill="none" stroke="var(--pink-deep)" stroke-width="5"/>
      <line x1="320" y1="232" x2="540" y2="160" stroke="var(--blue)" stroke-width="3"/>
      <line x1="340" y1="240" x2="540" y2="172" stroke="var(--blue)" stroke-width="2"/>
    </svg>
    <div class="brand">
      <span class="brand__dot"></span>
      <span class="brand__name">Mina Motion</span>
    </div>
    <p class="contact">0427 395 108<br>minaharper27@quillbox.net</p>
  </section>

  <section class="card card--back" aria-label="Card back">
    <svg class="card__shapes" viewBox="0 0 540 310" aria-hidden="true">
      <path d="M380,0 L540,0 L540,310 L180,310 Q470,250 475,130 Q478,40 380,0 Z" fill="var(--pink)"/>
      <path d="M380,0 Q478,40 475,130 Q470,250 180,310" fill="none" stroke="var(--pink-deep)" stroke-width="5"/>
      <line x1="0" y1="46" x2="420" y2="6" stroke="var(--blue)" stroke-width="3"/>
      <line x1="40" y1="300" x2="360" y2="262" stroke="var(--blue)" stroke-width="3"/>
      <line x1="60" y1="306" x2="380" y2="270" stroke="var(--blue)" stroke-width="2"/>
    </svg>
    <ul class="services">
      <li>Boxing for Fitness</li>
      <li>Aqua Fitness Professional</li>
      <li>PersonalisedTraining 1/1 or Small Group outdoor training</li>
      <li>Fun and unique workouts</li>
      <li>Weight loss/ Strength training</li>
    </ul>
    <p class="contact">0427 395 108<br>minaharper27@quillbox.net</p>
  </section>

</main>
</body>
</html>
```